Stationery Design Project

We are interested in A4 paper letterheads, envelopes, maybe A4 folders where we can put the patients' results in and businesscards. No information will be given out for the time being.
We would like to see mainly shades of white.. please refer to
http://en.brivola.org/wiki/Category:Tints_of_pale
anti-flash white, splashed white,ghost white, ivory, snow and white smoke or even light grey
we are interested mainly on the silver design but we welcome the other colors as well. Since its about a gynecologist please avoid dark colors, instead use shades of beige, light grey and white

```html
<!DOCTYPE html>
<html lang="id">
<head>
<meta charset="utf-8">
<title>Serelle – Stationery Set</title>
<link href="https://fonts.googleapis.com/css2?family=Open+Sans:wght@400;600&family=Arimo:wght@400&display=swap" rel="stylesheet">
<style>
  :root {
    --backdrop: #ecebe8;
    --paper: #f8f8f6;
    --pink: #f2e1e7;
    --silver: #b9bdc1;
    --silver-dark: #8e9398;
    --ink: #5b5e62;
    --letter-ink: #1f1f1f;
  }
  * { box-sizing: border-box; margin: 0; padding: 0; }
  html, body { width: 1200px; height: 840px; overflow: hidden; }
  body {
    background: var(--backdrop);
    font-family: "Open Sans", sans-serif;
    color: var(--ink);
    position: relative;
  }
  .sheet {
    position: absolute;
    background: var(--paper);
    overflow: hidden;
    box-shadow: 0 2px 8px rgba(0,0,0,.12);
  }
  .wave { position: absolute; left: 0; width: 100%; }
  .wave .fill { fill: var(--pink); }
  .wave .line { fill: none; stroke: url(#silverStroke); stroke-width: 5; vector-effect: non-scaling-stroke; }
  .wordmark {
    position: absolute;
    display: flex; align-items: center; gap: 8px;
    font-weight: 400; color: var(--silver-dark);
    letter-spacing: .04em;
    z-index: 1;
  }
  .wordmark .dot {
    width: 12px; height: 12px; border-radius: 50%;
    background: var(--silver);
  }
  .contact { position: absolute; font-size: 10px; line-height: 1.45; color: var(--ink); z-index: 1; }
  .contact .row { display: flex; align-items: center; gap: 6px; }
  .contact svg { width: 9px; height: 9px; stroke: var(--ink); fill: none; stroke-width: 1.4; flex: none; }
  .web { position: absolute; font-size: 10px; color: var(--ink); z-index: 1; }

  /* Letterhead */
  .letterhead { left: 40px; top: 66px; width: 500px; height: 707px; }
  .letterhead .wave { bottom: 0; height: 250px; }
  .letterhead .wordmark { left: 44px; top: 64px; font-size: 20px; }
  .letterhead .contact { right: 60px; top: 36px; font-size: 8px; }
  .letterhead .contact svg { width: 7px; height: 7px; }
  .letter-body {
    position: absolute; left: 44px; top: 150px; width: 400px;
    font-family: "Arimo", sans-serif; font-size: 11px; line-height: 1.5; color: var(--letter-ink);
  }
  .letter-body p { margin-bottom: 14px; }
  .letterhead .web { right: 40px; bottom: 76px; }

  /* Envelope back */
  .envelope-back { left: 580px; top: 50px; width: 580px; height: 250px; }
  .envelope-back .flap { position: absolute; left: 0; top: 0; width: 100%; height: 120px; }
  .envelope-back .flap path { fill: var(--pink); }
  .envelope-back .wordmark { left: 50%; top: 36px; transform: translateX(-50%); font-size: 18px; }
  .envelope-back .web { left: 50%; top: 72px; transform: translateX(-50%); }

  /* Envelope front */
  .envelope-front { left: 580px; top: 326px; width: 580px; height: 260px; }
  .envelope-front .wave { top: 0; height: 100%; }
  .envelope-front .wordmark { left: 36px; top: 32px; font-size: 18px; }
  .envelope-front .contact { left: 250px; top: 162px; font-size: 9.5px; line-height: 1.4; }

  /* Business cards */
  .card { width: 280px; height: 160px; top: 614px; }
  .card-back { left: 580px; background: var(--pink); }
  .card-back .wordmark { left: 50%; top: 50%; transform: translate(-50%,-50%); font-size: 18px; }
  .card-front { left: 880px; }
  .card-front .wave { top: 0; height: 100%; }
  .card-front .wordmark { left: 18px; top: 88px; font-size: 14px; }
  .card-front .identity { position: absolute; left: 138px; top: 10px; z-index: 1; }
  .card-front .name { font-size: 12px; font-weight: 600; color: var(--ink); letter-spacing: .03em; line-height: 1.3; }
  .card-front .role { font-size: 8px; margin-bottom: 4px; }
  .card-front .contact { position: static; font-size: 8px; line-height: 1.3; }
  .card-front .contact svg { width: 7px; height: 7px; }
  .card-front .web { left: 18px; bottom: 9px; font-size: 8.5px; }
</style>
</head>
<body>

<svg width="0" height="0" style="position:absolute">
  <defs>
    <linearGradient id="silverStroke" x1="0" x2="1" y1="0" y2="0">
      <stop offset="0" stop-color="#e4e6e8"/>
      <stop offset=".45" stop-color="#a9adb2"/>
      <stop offset=".75" stop-color="#d7d9dc"/>
      <stop offset="1" stop-color="#b4b8bc"/>
    </linearGradient>
    <symbol id="icon-phone" viewBox="0 0 10 10"><circle cx="5" cy="5" r="4"/><path d="M3.5 3.2 Q3.5 6.5 6.8 6.5"/></symbol>
    <symbol id="icon-fax" viewBox="0 0 10 10"><rect x="1.5" y="2" width="7" height="6"/><path d="M3 4h4M3 6h4"/></symbol>
    <symbol id="icon-mail" viewBox="0 0 10 10"><rect x="1" y="2.5" width="8" height="5"/><path d="M1 2.5 5 5.5 9 2.5"/></symbol>
  </defs>
</svg>

<!-- A4 letterhead -->
<section class="sheet letterhead">
  <div class="wordmark"><span class="dot"></span>Serelle</div>
  <div class="contact">
    <div>000 City Ave.</div>
    <div>PO Box 000</div>
    <div>State Heights, NN 00000</div>
    <div class="row"><svg><use href="#icon-phone"/></svg>(000) 000-0000</div>
    <div class="row"><svg><use href="#icon-fax"/></svg>(000) 000-0000</div>
    <div class="row"><svg><use href="#icon-mail"/></svg>hello@serellecare.com</div>
  </div>
  <div class="letter-body">
    <p>Jakarta, 18 Desember 2011</p>
    <p>Kepada<br>Yth. Mr. Adrian Wells<br>Jl. Melati No. 12, Jakarta</p>
    <p>Dengan hormat, kami sampaikan hasil pemeriksaan rutin Anda bersama surat ini. Mohon dibaca dengan saksama dan hubungi klinik kami bila ada pertanyaan mengenai jadwal kontrol berikutnya.</p>
  </div>
  <svg class="wave" viewBox="0 0 100 100" preserveAspectRatio="none">
    <path class="fill" d="M0 100 L0 78 C30 98 60 40 100 8 L100 100 Z"/>
    <path class="line" d="M0 78 C30 98 60 40 100 8"/>
  </svg>
  <div class="web">www.serellecare.com</div>
</section>

<!-- Envelope, back -->
<section class="sheet envelope-back">
  <svg class="flap" viewBox="0 0 100 100" preserveAspectRatio="none">
    <path d="M0 0 H100 V86 Q100 100 96 100 H4 Q0 100 0 86 Z"/>
  </svg>
  <div class="wordmark"><span class="dot"></span>Serelle</div>
  <div class="web">www.serellecare.com</div>
</section>

<!-- Envelope, front -->
<section class="sheet envelope-front">
  <div class="wordmark"><span class="dot"></span>Serelle</div>
  <svg class="wave" viewBox="0 0 100 100" preserveAspectRatio="none">
    <path class="fill" d="M0 100 L0 70 C35 72 60 30 100 12 L100 100 Z"/>
    <path class="line" d="M0 70 C35 72 60 30 100 12"/>
  </svg>
  <div class="contact">
    <div>000 City Ave.</div>
    <div>PO Box 000</div>
    <div>State Heights, NN 00000</div>
    <div class="row"><svg><use href="#icon-phone"/></svg>(000) 000-0000</div>
    <div class="row"><svg><use href="#icon-fax"/></svg>(000) 000-0000</div>
    <div class="row"><svg><use href="#icon-mail"/></svg>hello@serellecare.com</div>
  </div>
</section>

<!-- Business card, back -->
<section class="sheet card card-back">
  <div class="wordmark"><span class="dot"></span>Serelle</div>
</section>

<!-- Business card, front -->
<section class="sheet card card-front">
  <svg class="wave" viewBox="0 0 100 100" preserveAspectRatio="none">
    <path class="fill" d="M0 100 L0 84 C35 97 70 84 100 72 L100 100 Z"/>
    <path class="line" d="M0 84 C35 97 70 84 100 72"/>
  </svg>
  <div class="wordmark"><span class="dot"></span>Serelle</div>
  <div class="identity">
    <div class="name">LIVIA HART</div>
    <div class="role">CEO / Founder</div>
    <div class="contact">
      <div>000 City Ave.</div>
      <div>PO Box 000</div>
      <div>State Heights, NN 00000</div>
      <div class="row"><svg><use href="#icon-phone"/></svg>(000) 000-0000</div>
      <div class="row"><svg><use href="#icon-fax"/></svg>(000) 000-0000</div>
      <div class="row"><svg><use href="#icon-mail"/></svg>hello@serellecare.com</div>
    </div>
  </div>
  <div class="web">www.serellecare.com</div>
</section>

</body>
</html>
```